Kindle the Quiet Summit is a guide to help individuals overcome obstacles that they face in their life. This book provides thought provoking concepts that allow individuals to work through challenges if their life. The cover needs to be powerful! It needs to speak to the reader of breaking free of problems and overcoming challenges.

Kindle The Quiet Summit
A Handbook for climbing past hardships and growing into the self you were destined to become.
By
Dr. Marcus J. Belcroft

```html
<!DOCTYPE html>
<html lang="en">
<head>
<meta charset="utf-8">
<title>Kindle The Quiet Summit — Book Cover</title>
<link rel="stylesheet" href="https://fonts.googleapis.com/css2?family=Arimo:wght@700&family=Cousine&display=swap">
<style>
  :root {
    --paper-light: #f8f7f1;
    --paper-mid: #cfccbb;
    --paper-dark: #86846c;
    --ink: #000000;
    --frame: #222222;
    --ribbon-magenta: #b24a9a;
    --ribbon-blue: #33479a;
    --ribbon-teal: #188585;
    --ribbon-green: #2aa84a;
    --ribbon-red: #e2332d;
  }
  html, body {
    margin: 0;
    padding: 0;
    width: 888px;
    height: 1200px;
    overflow: hidden;
  }
  .cover {
    position: relative;
    width: 888px;
    height: 1200px;
    box-sizing: border-box;
    border: 1px solid var(--frame);
    background: linear-gradient(150deg, var(--paper-light) 0%, var(--paper-mid) 50%, var(--paper-dark) 100%);
    color: var(--ink);
  }
  .cover-art {
    position: absolute;
    left: 0;
    top: 80px;
    width: 830px;
    height: 250px;
  }
  .title {
    margin: 0;
    font-family: "Arimo", Arial, sans-serif;
    font-weight: 700;
    line-height: 1;
  }
  .title-line {
    position: absolute;
    display: block;
    white-space: nowrap;
    font-size: 70px;
    letter-spacing: -1px;
  }
  .title-line--1 { left: 265px; top: 386px; }
  .title-line--2 { left: 278px; top: 456px; }
  .title-line--3 { left: 380px; top: 528px; }
  .title-line--4 { left: 250px; top: 585px; font-size: 95px; letter-spacing: -1.5px; }
  .subtitle,
  .byline {
    position: absolute;
    left: 0;
    width: 888px;
    margin: 0;
    text-align: center;
    font-family: "Cousine", "Courier New", monospace;
    font-size: 22px;
    line-height: 27px;
  }
  .subtitle { top: 703px; }
  .byline { top: 1015px; left: -12px; }
</style>
</head>
<body>
  <main class="cover">
    <svg class="cover-art" role="img" aria-label="Illustration of a black fish trailing a rainbow-coloured ribbon across the top of the cover" viewBox="0 0 830 250">
      <defs>
        <linearGradient id="ribbon-tones" x1="0" y1="0" x2="1" y2="0">
          <stop offset="0" stop-color="var(--ribbon-magenta)"/>
          <stop offset="0.2" stop-color="var(--ribbon-blue)"/>
          <stop offset="0.35" stop-color="var(--ribbon-teal)"/>
          <stop offset="0.5" stop-color="var(--ribbon-green)"/>
          <stop offset="0.64" stop-color="var(--ribbon-red)"/>
          <stop offset="0.72" stop-color="var(--ink)"/>
          <stop offset="1" stop-color="var(--ink)"/>
        </linearGradient>
      </defs>
      <rect x="0" y="0" width="830" height="250" rx="24" fill="url(#ribbon-tones)" opacity="0.35"/>
    </svg>

    <h1 class="title">
      <span class="title-line title-line--1">Kindle</span>
      <span class="title-line title-line--2">The</span>
      <span class="title-line title-line--3">Quiet</span>
      <span class="title-line title-line--4">Summit</span>
    </h1>

    <p class="subtitle">A Handbook for climbing past hardships<br>and growing into the self you were destined to become.</p>

    <p class="byline">By<br>Dr. Marcus J. Belcroft</p>
  </main>
</body>
</html>
```